Trovadel Ltda

Logo design focused on: - Construction of civil works - Electrical services - Metal structures - Equipment rental Tomas Ibarra Luque Manager trovadel.ltda@norvexmail.com 56 9 41827035 Quirobamba s / n, Tolvas, San Pedro de Atacama

Target Market(s)

Building

Colors
33a6d7
0292cd
33b8a4
0555a3

```html
<!DOCTYPE html>
<html lang="es">
<head>
<meta charset="utf-8">
<title>Trovadel Ltda – Tarjetas de presentación</title>
<link href="https://fonts.googleapis.com/css2?family=Cinzel:wght@400&family=Montserrat:wght@400;600;700&display=swap" rel="stylesheet">
<style>
  :root{
    --bg:#e9ebee;
    --brand-blue:#0a74c4;
    --deep-blue:#0555a3;
    --sky:#33a6d7;
    --teal:#33b8a4;
    --ink:#444a52;
    --paper:#ffffff;
  }
  *{margin:0;padding:0;box-sizing:border-box}
  html,body{width:1200px;height:930px;overflow:hidden;background:var(--bg)}
  .canvas{position:relative;width:1200px;height:930px}
  .card{position:absolute;width:600px;height:343px;overflow:hidden;box-shadow:0 6px 18px rgba(0,0,0,.18)}

  /* Back side */
  .card--back{left:80px;top:70px;background:var(--brand-blue)}
  .card--back .emblem-disc{position:absolute;right:44px;top:22px;width:214px;height:214px;border-radius:50%;background:var(--teal)}
  .card--back .brand{position:absolute;left:34px;bottom:36px;display:flex;align-items:center;gap:12px}
  .card--back .brand-dot{width:46px;height:46px;border-radius:50%;background:var(--paper)}
  .card--back .brand-name{font-family:'Cinzel',serif;font-size:28px;color:var(--paper);letter-spacing:1px;line-height:1}

  /* Front side */
  .card--front{left:520px;top:500px;background:var(--paper)}
  .card--front .brand{position:absolute;left:32px;top:32px;display:flex;align-items:center;gap:12px}
  .card--front .brand-dot{width:50px;height:50px;border-radius:50%;background:var(--sky)}
  .card--front .brand-name{font-family:'Cinzel',serif;font-size:30px;color:var(--brand-blue);letter-spacing:1px;line-height:1}

  .contact{position:absolute;left:36px;top:150px;font-family:'Montserrat',sans-serif}
  .contact .person{font-weight:700;font-size:21px;color:var(--deep-blue)}
  .contact .role{font-weight:700;font-size:18px;color:var(--teal);margin-bottom:14px}
  .contact p{font-size:13px;color:var(--ink);line-height:1.45}
  .contact .line{display:flex;align-items:center;gap:10px;margin-top:2px}
  .contact .line svg{width:14px;height:14px;flex:none}

  .services{position:absolute;right:30px;top:110px;list-style:none;font-family:'Montserrat',sans-serif;font-size:14px;color:var(--ink);text-align:right}
  .services li{display:flex;justify-content:flex-end;align-items:center;gap:10px;line-height:1.6}
  .services li::after{content:"";width:7px;height:7px;background:var(--sky)}

  .swoosh{position:absolute;right:0;bottom:0;width:600px;height:343px}
</style>
</head>
<body>
<main class="canvas">

  <section class="card card--back" aria-label="Reverso de la tarjeta">
    <div class="emblem-disc"></div>
    <div class="brand">
      <span class="brand-dot"></span>
      <span class="brand-name">TROVADEL Ltda</span>
    </div>
  </section>

  <section class="card card--front" aria-label="Anverso de la tarjeta">
    <svg class="swoosh" viewBox="0 0 600 343" preserveAspectRatio="none" aria-hidden="true">
      <path d="M330 343 C430 300 520 240 600 218 L600 343 Z" fill="var(--teal)"/>
      <path d="M395 343 C470 305 540 260 600 240 L600 343 Z" fill="var(--paper)"/>
      <path d="M405 343 C478 308 545 266 600 248 L600 343 Z" fill="var(--brand-blue)"/>
    </svg>

    <div class="brand">
      <span class="brand-dot"></span>
      <span class="brand-name">TROVADEL Ltda</span>
    </div>

    <div class="contact">
      <div class="person">Tomas Ibarra Luque</div>
      <div class="role">Gerente</div>
      <p>Quirobamba s/n, Tolvas,<br>San Pedro de Atacama</p>
      <p class="line">
        <svg viewBox="0 0 24 24"><path d="M6.6 10.8a15 15 0 0 0 6.6 6.6l2.2-2.2a1 1 0 0 1 1-.25 11.4 11.4 0 0 0 3.6.57 1 1 0 0 1 1 1V20a1 1 0 0 1-1 1A17 17 0 0 1 3 4a1 1 0 0 1 1-1h3.5a1 1 0 0 1 1 1c0 1.25.2 2.450.57 3.57a1 1 0 0 1-.25 1z" fill="var(--brand-blue)"/></svg>
        +56 9 41827035
      </p>
      <p class="line">
        <svg viewBox="0 0 24 24"><rect x="3" y="5" width="18" height="14" rx="1.5" fill="none" stroke="var(--brand-blue)" stroke-width="2"/><path d="M3.5 6l8.5 7 8.5-7" fill="none" stroke="var(--brand-blue)" stroke-width="2"/></svg>
        trovadel.ltda@norvexmail.com
      </p>
    </div>

    <ul class="services">
      <li>Construcción de Obras Civiles</li>
      <li>Servicios eléctricos</li>
      <li>Estructuras metálicas</li>
      <li>Arriendo de Equipos</li>
    </ul>
  </section>

</main>
</body>
</html>
```